Company director needs a business card design

I am a semi-retired former senior finance executive who sits on a number of public and private company boards and do some consulting work. I work largely with emerging businesses but deal regularly with top end of town lawyers, bankers etc. I need a thoughtful but relatively conservative design which would also resonate with my younger client base. Some colour would be good. Information limited to name, address, office tel, mobile and email.

Industry/Entity Type

Finance

```html
<!DOCTYPE html>
<html lang="en">
<head>
<meta charset="utf-8">
<title>Daniel Whitford – Business Card</title>
<link rel="stylesheet" href="https://fonts.googleapis.com/css2?family=Fira+Sans:wght@300;400;600&display=swap">
<style>
  :root {
    --backdrop: #e6e6e6;
    --paper: #ffffff;
    --navy-card: #075c9b;
    --blue-light: #a8cde8;
    --blue-mid: #4a9bd6;
    --blue-dark: #1a6fb5;
    --blue-deep: #0a3c6e;
    --name-blue: #3f9ad6;
    --ink: #222222;
    --ink-on-blue: #0c2b4a;
    --accent: #f08a3c;
    --emblem-light: #eeeff1;
    --emblem-dark: #0a6cb0;
  }
  * { margin: 0; padding: 0; box-sizing: border-box; }
  html, body { width: 900px; height: 1200px; overflow: hidden; }
  body {
    background: var(--backdrop);
    font-family: "Fira Sans", Arial, sans-serif;
    position: relative;
  }
  .card {
    position: absolute;
    left: 67px;
    width: 768px;
    height: 474px;
    overflow: hidden;
    box-shadow: 0 3px 8px rgba(0,0,0,0.25);
  }
  .card--front { top: 80px; background: var(--paper); }
  .card--reverse { top: 636px; background: var(--navy-card); }

  .emblem-circle {
    position: absolute;
    left: 473px;
    top: 25px;
    width: 300px;
    height: 300px;
    border-radius: 50%;
  }
  .card--front .emblem-circle { background: var(--emblem-light); }
  .card--reverse .emblem-circle { background: var(--emblem-dark); }

  .stripe {
    position: absolute;
    width: 8px;
  }
  .stripe--a { left: 50px; }
  .stripe--b { left: 63px; }
  .stripe--c { left: 76px; }
  .stripes-top .stripe { top: 0; height: 236px; }
  .stripes-bottom .stripe { top: 334px; height: 140px; }
  .stripes-bottom .stripe--b { top: 324px; }

  .card--front .stripe--a { background: var(--blue-light); }
  .card--front .stripe--b { background: var(--blue-mid); }
  .card--front .stripe--c { background: var(--blue-dark); }
  .card--reverse .stripe--a { background: #ffffff; }
  .card--reverse .stripe--b { background: var(--blue-mid); }
  .card--reverse .stripe--c { background: var(--blue-deep); }

  .name {
    position: absolute;
    left: 50px;
    top: 248px;
    font-size: 59px;
    line-height: 1;
    white-space: nowrap;
    letter-spacing: -0.3px;
  }
  .name__first { font-weight: 400; }
  .name__last { font-weight: 600; position: relative; }
  .card--front .name { color: var(--name-blue); }
  .card--reverse .name { color: #ffffff; }
  .dotted-i { position: relative; }
  .dotted-i::after {
    content: "";
    position: absolute;
    left: 50%;
    top: 2px;
    width: 10px;
    height: 10px;
    margin-left: -5px;
    border-radius: 50%;
    background: var(--accent);
  }

  .contact {
    position: absolute;
    left: 98px;
    top: 340px;
    font-size: 29px;
    font-weight: 300;
    line-height: 41px;
    white-space: pre;
  }
  .card--front .contact { color: var(--ink); }
  .card--reverse .contact { color: var(--ink-on-blue); }

  .email {
    position: absolute;
    right: 37px;
    bottom: 34px;
    writing-mode: vertical-rl;
    transform: rotate(180deg);
    font-size: 27px;
    font-weight: 300;
    white-space: nowrap;
  }
  .card--front .email { color: var(--ink); }
  .card--reverse .email { color: #e8f0f8; }
  .email__initial { color: var(--accent); }
</style>
</head>
<body>

  <section class="card card--front">
    <div class="emblem-circle" role="img" aria-label="Faint monogram emblem area"></div>
    <div class="stripes-top">
      <span class="stripe stripe--a"></span><span class="stripe stripe--b"></span><span class="stripe stripe--c"></span>
    </div>
    <div class="stripes-bottom">
      <span class="stripe stripe--a"></span><span class="stripe stripe--b"></span><span class="stripe stripe--c"></span>
    </div>
    <h1 class="name"><span class="name__first">Daniel</span> <span class="name__last">Wh<span class="dotted-i">ı</span>tford</span></h1>
    <p class="contact">18 Carrow Street,    Seaview   NSW  2099
Tel: (02) 9340 5182   Mobile: 0412 555 708</p>
    <p class="email"><span class="email__initial">d</span>aniel_<span class="email__initial">w</span>hitford@mailbox.net.au</p>
  </section>

  <section class="card card--reverse">
    <div class="emblem-circle" role="img" aria-label="Faint monogram emblem area"></div>
    <div class="stripes-top">
      <span class="stripe stripe--a"></span><span class="stripe stripe--b"></span><span class="stripe stripe--c"></span>
    </div>
    <div class="stripes-bottom">
      <span class="stripe stripe--a"></span><span class="stripe stripe--b"></span><span class="stripe stripe--c"></span>
    </div>
    <h2 class="name"><span class="name__first">Daniel</span> <span class="name__last">Wh<span class="dotted-i">ı</span>tford</span></h2>
    <p class="contact">18 Carrow Street,    Seaview   NSW  2099
Tel: (02) 9340 5182   Mobile: 0412 555 708</p>
    <p class="email"><span class="email__initial">d</span>aniel_<span class="email__initial">w</span>hitford@mailbox.net.au</p>
  </section>

</body>
</html>
```